Concierge Healthcare Business Card Design and Logo

We need a logo and business card design for a new company called "Sound Harbor". We will provide concierge audiological care, hearing aids, hearing exams, custom hearing protection etc to patients in the comfort of their homes and offices. We would like a sleek and modern design preferably with an Ear related logo.

Target Market(s)

People with hearing loss, Hunters, Musicians
My usual clientele are older individuals so usually 50+ years old

Industry/Entity Type

Health Care

Contact Information for Business Card

Delia Franks, AuD
Audiologist
512-648-2917
soundharbor@mailnest.com
www.soundharbor-example.com

Logo Text

Sound Harbor

Number of Pages Required

3 page

```html
<!DOCTYPE html>
<html lang="en">
<head>
<meta charset="utf-8">
<title>Sound Harbor – Business Card</title>
<link rel="stylesheet" href="https://fonts.googleapis.com/css2?family=Mulish:wght@400;700&display=swap">
<style>
  :root {
    --backdrop: #e6e6e8;
    --card: #ffffff;
    --ink: #4a4a4a;
    --ink-soft: #5c5c5c;
    --rule: #6a6a6a;
    --shadow: rgba(0, 0, 0, 0.12);
  }
  * { box-sizing: border-box; margin: 0; padding: 0; }
  html, body {
    width: 1200px;
    height: 800px;
    overflow: hidden;
    background: var(--backdrop);
    font-family: "Mulish", "Century Gothic", sans-serif;
    color: var(--ink);
  }
  .sheet {
    width: 1200px;
    height: 800px;
    display: flex;
    flex-direction: column;
    align-items: center;
    justify-content: center;
    gap: 40px;
  }
  .card {
    width: 600px;
    height: 343px;
    background: var(--card);
    box-shadow: 0 4px 14px var(--shadow);
    position: relative;
  }
  .brand {
    display: flex;
    flex-direction: column;
    align-items: center;
  }
  .brand__mark {
    width: 44px;
    height: 44px;
    border: 3px solid var(--ink);
    border-radius: 50%;
    margin-bottom: 14px;
  }
  .brand__name {
    font-weight: 700;
    font-size: 24px;
    letter-spacing: 0.5px;
    text-transform: uppercase;
    color: var(--ink);
    white-space: nowrap;
  }
  .brand__url {
    font-weight: 700;
    font-size: 11px;
    margin-top: 4px;
    color: var(--ink);
  }
  .card--front {
    display: flex;
    align-items: center;
    justify-content: center;
  }
  .card--back .brand {
    position: absolute;
    left: 30px;
    width: 250px;
    top: 110px;
  }
  .divider {
    position: absolute;
    left: 300px;
    top: 70px;
    width: 2px;
    height: 200px;
    background: var(--rule);
  }
  .contact {
    position: absolute;
    left: 334px;
    top: 78px;
  }
  .contact__name {
    font-weight: 700;
    font-size: 18px;
    color: var(--ink);
  }
  .contact__role {
    font-size: 16px;
    margin-top: 4px;
    color: var(--ink-soft);
  }
  .contact__details {
    margin-top: 40px;
    font-size: 16px;
    line-height: 1.3;
    color: var(--ink-soft);
  }
</style>
</head>
<body>
  <main class="sheet">
    <section class="card card--front" aria-label="Card front">
      <div class="brand">
        <span class="brand__mark" aria-hidden="true"></span>
        <span class="brand__name">Sound Harbor</span>
        <span class="brand__url">www.soundharbor-example.com</span>
      </div>
    </section>

    <section class="card card--back" aria-label="Card back">
      <div class="brand">
        <span class="brand__mark" aria-hidden="true"></span>
        <span class="brand__name">Sound Harbor</span>
        <span class="brand__url">www.soundharbor-example.com</span>
      </div>
      <span class="divider" aria-hidden="true"></span>
      <div class="contact">
        <p class="contact__name">Delia Franks, AuD</p>
        <p class="contact__role">Audiologist</p>
        <p class="contact__details">
          512-648-2917<br>
          soundharbor@mailnest.com
        </p>
      </div>
    </section>
  </main>
</body>
</html>
```